Psychotherapy Website - Based in London

I am a newly trained psychotherapist and need a new website for www.rosalindfaber.co.uk.

I offer therapy for addiction, relationships, trauma and many other issues people face in their lives.

I want the website to be welcoming, gentle, feminine and for people to feel safe.

I do not like a page site that scrolls through sections, rather each page should be separate. Here some examples that i like. Sectional rather than scrolled.

https://www.hettiemarsh.com/
https://www.thequietwardrooms.com/

The imagery should be around pink using the flower in the logo / wording and around the site:

Here is a link to the flower for ideas:
https://www.pictofind.net/search?q=pink+gerbera&rlz=2D4KQTW_en-GBGB415GB415&source=lnms&tbm=isch&sa=X&ved=7cvQRtrk482h3PxZTuKLmeNBwXW_1AtXpVlKDbOQBmFLB&biw=1500&bih=889&dpr=2

RosalindFaber
Compassionate Psychotherapy

Is the logo and subheader for the website. Please use a typeface for the name that is appealing and professional.

Type face similar NOT EXLUSIVLY - JUST AN IDEA like this:
https://glowtonicstudio.com/

Basic business card i created as a rough idea below.

I have also added the website copy.

The headers are

Homepage
About Me
Therapy
Common Questions
Blog
Contact Me

Target Market(s)

Clients who are dealing with stress, trauma, pain, addiction

Industry/Entity Type

Therapy and Psychology

Coding

Coded - Design and coding required

Number of Pages Required

5+ page

Font styles to use
Serif
Sans Serif
Script

Colors
0054AA
0677BA
7BADD7
CADEEF
E8F1F8
0094D4
00A9DD
6FCCEA
C7EBF8
E9F6FB
E54698
E96AAD
F1A4CE
F9D9EA
FCEFF6

Requirements
Must have
• Pink Gerbera Flower integrated into design
Nice to have
• Images but not to stock imagery. Needs to look authentic and natural
Should not have
• Stock images of people. Images are important but needs to feel REAL

```html
<!DOCTYPE html>
<html lang="en">
<head>
<meta charset="utf-8">
<title>Trainee Psychotherapist Rosalind Faber</title>
<link rel="stylesheet" href="https://fonts.googleapis.com/css2?family=Playfair+Display:wght@400;500&family=Roboto:wght@400;500;700&display=swap">
<style>
:root{
  --pink:#e54698;
  --pink-mid:#e96aad;
  --pink-soft:#f1a4ce;
  --pink-pale:#f9d9ea;
  --pink-wash:#fceff6;
  --blog-bg:#f6c4dc;
  --btn-a:#d23d8f;
  --btn-b:#7a2f9f;
  --ink:#1e1e1e;
  --text:#333;
  --muted:#555;
  --footer:#121212;
  --mauve:#a88398;
}
*{box-sizing:border-box;margin:0;padding:0}
html,body{width:1200px;height:4161px;overflow:hidden}
body{position:relative;background:#fff;font-family:"Roboto",Arial,sans-serif;color:var(--text)}
.abs{position:absolute}
.serif{font-family:"Playfair Display",Georgia,serif}
.btn{position:absolute;display:flex;align-items:center;justify-content:center;border-radius:30px;
  background:linear-gradient(110deg,var(--btn-a),var(--btn-b));color:#fff;font-size:17px;font-weight:500;letter-spacing:.5px;
  box-shadow:0 0 0 3px rgba(255,255,255,.55)}
.rule{display:block;width:52px;height:3px;background:var(--pink);margin:14px auto 0}

/* hero */
.hero{position:absolute;left:0;top:0;width:1200px;height:705px;overflow:hidden}
.hero-photo{position:absolute;inset:0;background:
  radial-gradient(ellipse 260px 330px at 930px 320px,#c9a68f 0%,rgba(201,166,143,0) 70%),
  linear-gradient(90deg,#8a7c7a 0%,#a09494 35%,#8d8482 60%,#6e6463 100%)}
.hero-shade{position:absolute;inset:0;background:rgba(40,30,40,.28)}
.nav{position:absolute;left:0;top:0;width:1200px;height:86px;background:rgba(45,45,48,.78)}
.nav a{position:absolute;top:30px;color:#fff;font-size:17px;text-decoration:none}
.nav a.active{color:var(--pink)}
.nav .line{position:absolute;top:43px;height:1px;width:50px;background:var(--pink)}
.logo{position:absolute;left:478px;top:16px;width:244px;height:57px;border:2px solid var(--pink);border-radius:6px;
  background:linear-gradient(90deg,#1b1b1b,#3a1028);color:#fff;font-weight:700;font-size:12px;letter-spacing:1.5px;
  text-align:center;padding-top:13px;line-height:14px}
.hero h1{position:absolute;left:110px;top:208px;width:620px;color:#fff;font-size:42px;font-weight:500;line-height:47px;letter-spacing:.5px}
.online{position:absolute;left:110px;top:390px;color:#fff;font-size:21px;font-weight:500;letter-spacing:.5px;display:flex;align-items:center}
.online i{width:22px;height:22px;border-radius:50%;background:var(--pink);margin-right:16px;box-shadow:0 0 0 3px rgba(255,255,255,.5)}
.dots{position:absolute;left:1141px;top:274px}
.dots span{display:block;width:3px;height:18px;background:var(--pink);margin-bottom:6px}
.dots span.on{background:#fff}

/* about */
.about h2{position:absolute;left:110px;top:766px;font-size:42px;font-weight:400;color:var(--ink)}
.about .tick{position:absolute;left:230px;top:803px;width:55px;height:3px;background:var(--pink)}
.about p{position:absolute;left:110px;width:500px;font-size:17px;line-height:30px;color:var(--text)}

/* therapy */
.therapy{position:absolute;left:0;top:1268px;width:1200px;height:996px;overflow:hidden}
.therapy-photo{position:absolute;inset:0;background:linear-gradient(90deg,#8f6f84 0%,#b7a0ad 30%,#c7b2bd 50%,#b39aa8 70%,#8b6b80 100%)}
.therapy-tint{position:absolute;inset:0;background:rgba(166,110,148,.45)}
.therapy h2{position:absolute;left:0;width:1200px;top:50px;text-align:center;color:#fff;font-size:40px;font-weight:400}
.therapy .intro{position:absolute;left:240px;width:720px;top:148px;text-align:center;color:#fff;font-size:17px;line-height:30px}
.card{position:absolute;width:252px;height:260px;background:#fff;border:2px solid var(--pink-soft);border-radius:4px;text-align:center}
.card.hl{background:linear-gradient(180deg,#fbe3ef,#f8d2e5)}
.card .icon{width:62px;height:62px;margin:18px auto 0;border-radius:50%;background:var(--pink-wash);border:2px solid var(--pink-soft)}
.card h3{font-family:"Playfair Display",Georgia,serif;font-weight:500;font-size:21px;color:var(--ink);margin-top:14px;letter-spacing:.5px}
.card h3::after{content:"";display:block;width:46px;height:2px;background:var(--pink);margin:9px auto 0}
.card p{font-size:17px;line-height:30px;color:#333;margin:14px 20px 0}

/* questions */
.qs h2{position:absolute;left:0;width:1200px;top:2342px;text-align:center;font-size:42px;font-weight:400;color:var(--ink);letter-spacing:1px}
.q{position:absolute;left:556px;width:536px;font-size:18px;color:#222;font-weight:500}
.qa{position:absolute;left:556px;width:536px;top:2530px;font-size:17px;line-height:30px;color:var(--muted)}
.qdiv{position:absolute;left:556px;width:536px;height:1px;background:#ddd}

/* blog */
.blog{position:absolute;left:0;top:2923px;width:1200px;height:890px;background:var(--blog-bg);overflow:hidden}
.blog-flower{position:absolute;left:820px;top:40px;width:520px;height:420px;border-radius:50%;background:radial-gradient(circle,#fbe0ec 0%,rgba(251,224,236,0) 70%)}
.blog h2{position:absolute;left:0;width:1200px;top:50px;text-align:center;font-size:42px;font-weight:400;color:var(--ink)}
.post{position:absolute;top:178px;width:386px;height:460px;background:#fff;border-radius:4px;box-shadow:0 4px 12px rgba(0,0,0,.12);overflow:hidden}
.post .img{height:250px}
.post .date{margin:24px 23px 0;font-size:15px;font-weight:700;color:var(--pink);letter-spacing:.5px}
.post h3{margin:12px 23px 0;font-size:20px;font-weight:500;color:#222;line-height:32px;padding-bottom:16px;border-bottom:1px solid #bbb}
.post p{margin:16px 23px 0;font-size:18px;line-height:32px;color:#444}

/* footer */
.footer{position:absolute;left:0;top:3806px;width:1200px;height:355px;background:var(--footer);color:#fff}
.footer h4{position:absolute;top:70px;font-family:"Playfair Display",Georgia,serif;font-weight:400;font-size:20px}
.footer h4::after{content:"";display:block;width:28px;height:2px;background:var(--pink);margin-top:8px}
.footer ul{position:absolute;list-style:none;top:122px;font-size:17px;line-height:30px}
.footer .copy{position:absolute;left:0;width:1200px;top:308px;text-align:center;font-size:17px}
.footer .sep{position:absolute;left:113px;width:974px;top:288px;height:1px;background:#333}
.contact li{display:flex;align-items:center}
.contact svg{margin-right:12px}
</style>
</head>
<body>

<section class="hero">
  <div class="hero-photo" role="img" aria-label="Smiling woman at a laptop in a bright living room with a cotton stem vase"></div>
  <div class="hero-shade"></div>
  <nav class="nav">
    <a class="active" style="left:135px">Home</a>
    <a style="left:202px">About Me</a>
    <a style="left:300px">Therapy</a>
    <span class="line" style="left:425px"></span>
    <div class="logo">TRAINEE PSYCHOTHERAPIST<br>ROSALIND FABER</div>
    <span class="line" style="left:727px"></span>
    <a style="left:839px">Questions</a>
    <a style="left:941px">Blog</a>
    <a style="left:997px">Contact</a>
  </nav>
  <h1 class="serif">A non-judgmental space where any issues can be explored in complete confidentiality</h1>
  <div class="online"><i></i>ONLINE THERAPY AVAILABLE</div>
  <a class="btn" style="left:110px;top:467px;width:176px;height:52px">GET A QUOTE</a>
  <div class="dots"><span></span><span class="on"></span><span></span></div>
  <svg class="abs" style="left:0;top:585px" width="1200" height="120" viewBox="0 0 1200 120">
    <defs><linearGradient id="heroEdge" x1="0" x2="1"><stop offset="0" stop-color="#5b2aa6"/><stop offset=".6" stop-color="#e54698"/><stop offset="1" stop-color="#6a2fb0"/></linearGradient></defs>
    <polygon points="0,5 197,117 1200,5 1200,120 0,120" fill="url(#heroEdge)"/>
    <polygon points="0,18 197,98 1200,18 1200,120 0,120" fill="#fff"/>
  </svg>
</section>

<section class="about">
  <h2 class="serif">About</h2>
  <span class="tick"></span>
  <p style="top:832px">Taking the first steps towards engaging in therapy can be a very personal journey.</p>
  <p style="top:901px">Whilst, it can be challenging, I will ensure to make this journey as safe and as comfortable for you as possible.</p>
  <p style="top:971px">Psychotherapy can help you see your current situation in new light, depth and clarity. It can change old and unhelpful perspectives and feelings about yourself and your life, and ultimately help you make positive changes.</p>
  <a class="btn" style="left:110px;top:1116px;width:176px;height:55px">LEARN MORE</a>
  <div class="abs" style="left:723px;top:797px;width:398px;height:398px;border-radius:50%;background:radial-gradient(circle at 60% 55%,#f6c6de,#fbe2ef 70%)"></div>
  <div class="abs" style="left:703px;top:787px;width:386px;height:386px;border-radius:50%;border:2px solid var(--pink-mid)"></div>
  <div class="abs" role="img" aria-label="Portrait of the psychotherapist" style="left:715px;top:791px;width:362px;height:362px;border-radius:50%;background:linear-gradient(160deg,#ece9e6,#d6c9c2 60%,#c96b8c)"></div>
</section>

<section class="therapy">
  <div class="therapy-photo" role="img" aria-label="Two women talking in a therapy room"></div>
  <div class="therapy-tint"></div>
  <h2 class="serif">Therapy</h2>
  <span class="abs" style="left:574px;top:110px;width:52px;height:3px;background:var(--pink)"></span>
  <p class="intro">I offer a range of psychotherapeutic approaches including transactional analysis psychotherapy and relational therapy.</p>
  <div class="card" style="left:181px;top:244px"><div class="icon" role="img" aria-label="Addiction icon"></div><h3>Addiction</h3><p>Nemo enim ipsam voluptatem quia voluptas sit aspernatur aut</p></div>
  <div class="card hl" style="left:473px;top:244px"><div class="icon" role="img" aria-label="Bullying icon"></div><h3>Bullying</h3><p>Nemo enim ipsam voluptatem quia voluptas sit aspernatur aut</p></div>
  <div class="card" style="left:766px;top:244px"><div class="icon" role="img" aria-label="Depression icon"></div><h3>Depression</h3><p>Nemo enim ipsam voluptatem quia voluptas sit aspernatur aut</p></div>
  <div class="card" style="left:181px;top:544px"><div class="icon" role="img" aria-label="Fear icon"></div><h3>Fear</h3><p>Nemo enim ipsam voluptatem quia voluptas sit aspernatur aut</p></div>
  <div class="card" style="left:473px;top:544px"><div class="icon" role="img" aria-label="Awareness ribbon icon"></div><h3>HIV</h3><p>Nemo enim ipsam voluptatem quia voluptas sit aspernatur aut</p></div>
  <div class="card" style="left:766px;top:544px"><div class="icon" role="img" aria-label="Stress icon"></div><h3>Stress</h3><p>Nemo enim ipsam voluptatem quia voluptas sit aspernatur aut</p></div>
  <a class="btn" style="left:481px;top:873px;width:236px;height:54px">VIEW ALL THERAPY</a>
</section>

<section class="qs">
  <h2 class="serif">Common Questions</h2>
  <span class="abs" style="left:574px;top:2413px;width:52px;height:3px;background:var(--pink)"></span>
  <div class="abs" style="left:76px;top:2442px;width:414px;height:414px;border-radius:50%;background:var(--pink-pale)"></div>
  <div class="abs" style="left:110px;top:2438px;width:390px;height:390px;border-radius:50%;border:2px solid var(--pink-mid)"></div>
  <div class="abs" role="img" aria-label="Couple in a counselling session with a therapist" style="left:118px;top:2446px;width:372px;height:372px;border-radius:50%;background:linear-gradient(160deg,#b9b7b2,#8c8a86 45%,#d4b53a 75%,#7a6e62)"></div>
  <div class="abs" role="img" aria-label="Pink gerbera flowers" style="left:86px;top:2690px;width:130px;height:130px;border-radius:50%;background:radial-gradient(circle,#c6304f 0%,#e0506e 35%,rgba(230,90,120,0) 72%)"></div>
  <div class="q" style="top:2488px">How long are the sessions?</div>
  <p class="qa">Typically, each session is 50 minutes provided in person at my practice in Richmond, or online using a platform such as Meetly or Callspace.</p>
  <span class="qdiv" style="top:2629px"></span>
  <div class="q" style="top:2651px">How long will I need therapy for?</div>
  <span class="qdiv" style="top:2690px"></span>
  <div class="q" style="top:2711px">How much is each session?</div>
  <a class="btn" style="left:554px;top:2773px;width:158px;height:54px">VIEW MORE</a>
</section>

<section class="blog">
  <div class="blog-flower" role="img" aria-label="Soft pink gerbera flower"></div>
  <h2 class="serif">Latest Blog</h2>
  <span class="abs" style="left:574px;top:115px;width:52px;height:3px;background:var(--pink)"></span>
  <article class="post" style="left:192px">
    <div class="img" role="img" aria-label="Two men talking in a counselling session" style="background:linear-gradient(160deg,#e8e6e2,#cfcac3 50%,#6f6a66)"></div>
    <div class="date">DATE: 10-12-21</div>
    <h3>Trauma and the bears – a fable</h3>
    <p>Once upon a time … there were humans on the savannah.</p>
  </article>
  <article class="post" style="left:622px">
    <div class="img" role="img" aria-label="Man with his head in his hand during therapy" style="background:linear-gradient(160deg,#f0eeec,#c9c4bf 50%,#5c6770)"></div>
    <div class="date">DATE: 10-12-21</div>
    <h3>Why the symptoms of trauma make sense</h3>
    <p>I looked again at the list of symptoms</p>
  </article>
  <a class="btn" style="left:520px;top:695px;width:158px;height:53px">VIEW MORE</a>
</section>

<svg class="abs" style="left:0;top:3690px" width="1200" height="120" viewBox="0 0 1200 120">
  <defs><linearGradient id="footEdge" x1="0" x2="1"><stop offset="0" stop-color="#5b2aa6"/><stop offset=".8" stop-color="#e54698"/><stop offset="1" stop-color="#7a2fa8"/></linearGradient></defs>
  <polygon points="0,118 1000,8 1200,36 1200,120 0,120" fill="url(#footEdge)"/>
  <polygon points="0,120 1000,26 1200,56 1200,120" fill="var(--footer)"/>
</svg>

<footer class="footer">
  <h4 style="left:113px">Quick links</h4>
  <ul style="left:113px"><li>Home</li><li>About Me</li><li>Therapy</li></ul>
  <ul style="left:234px"><li>Questions</li><li>Blog</li><li>Contact</li></ul>
  <h4 style="left:450px">Address</h4>
  <ul style="left:450px" class="contact">
    <li><svg width="12" height="16" viewBox="0 0 12 16"><path d="M6 0a6 6 0 0 0-6 6c0 4.5 6 10 6 10s6-5.5 6-10a6 6 0 0 0-6-6zm0 8.5A2.5 2.5 0 1 1 6 3.5a2.5 2.5 0 0 1 0 5z" fill="#fff"/></svg>Elmwood Community Centre</li>
    <li style="padding-left:24px">27 Larkfield Road</li>
    <li style="padding-left:24px">East Twickenham</li>
    <li style="padding-left:24px">TW1 4QD</li>
  </ul>
  <h4 style="left:786px">Contact Us</h4>
  <ul style="left:786px" class="contact">
    <li><svg width="15" height="15" viewBox="0 0 16 16"><circle cx="8" cy="8" r="7" fill="none" stroke="#fff" stroke-width="1.5"/><path d="M1 8h14M8 1c-3 3-3 11 0 14M8 1c3 3 3 11 0 14" fill="none" stroke="#fff" stroke-width="1.3"/></svg>www.rosalindfaber.co.uk</li>
    <li><svg width="15" height="12" viewBox="0 0 16 12"><rect width="16" height="12" rx="1.5" fill="#fff"/><path d="M1 1.5l7 5 7-5" fill="none" stroke="#121212" stroke-width="1.4"/></svg>hello@rosalindfaber.co.uk</li>
    <li><svg width="15" height="15" viewBox="0 0 16 16"><path d="M3.5 0.8l2.4 2.9-1.4 2.2c.9 2 2.6 3.7 4.6 4.6l2.2-1.4 2.9 2.4-1.2 3.1C6.7 14.7 1.3 9.3.4 2z" fill="#fff"/></svg>07700 900418</li>
  </ul>
  <span class="sep"></span>
  <div class="copy">2021 Trainee Psychotherapist Rosalind Faber</div>
</footer>

</body>
</html>
```